Lanternwake Tales - A podcast of inspiring stories of people living a heart centred life

We need a thumbnail to use on Podvane for our podcast 'Lanternwake Tales'.

Each week Rosalind Pettigrew & Wendy Tulloch interview inspirational people who have come from a place of adversity to living a truly inspired life.

From animal healing to breaking through the lowest of lows - Lanternwake tales brings together people who are on a journey living a heart centred life.

Purples, greens, yellows, and pinks are our preference.

Reason: The designs provided aren't appropriate. Elegant and Professional is what we're after.

Target Market(s)

People searching for meaning in life - self help book readers.

Colors
33b8a4
abd037
fbee3e
ffcf3e
faa54b
fef6f0
f04a50
e34197
f37122

Requirements
Must have
• Striking colours.
Nice to have
• Blended colours are preferred over blocks. But we're open to suggestions.
Should not have
• Overused podcast themes.

```html
<!DOCTYPE html>
<html lang="en">
<head>
<meta charset="utf-8">
<title>Lanternwake Tales – Podcast Cover</title>
<link rel="stylesheet" href="https://fonts.googleapis.com/css2?family=Saira+Extra+Condensed:wght@700&display=swap">
<style>
  :root {
    --pink: #e34197;
    --red: #f04a50;
    --orange: #f37122;
    --apricot: #faa54b;
    --gold: #ffcf3e;
    --lemon: #fbee3e;
    --lime: #abd037;
    --teal: #33b8a4;
    --cream: #fef6f0;
    --white: #ffffff;
  }
  html, body {
    margin: 0;
    padding: 0;
    width: 1200px;
    height: 1200px;
    overflow: hidden;
    background: var(--white);
  }
  .cover {
    position: relative;
    width: 1200px;
    height: 1200px;
    overflow: hidden;
    background: linear-gradient(
      to bottom,
      #e84a6e 0%,
      var(--red) 6%,
      #f2603a 14%,
      var(--orange) 24%,
      var(--apricot) 34%,
      var(--gold) 46%,
      #fce640 56%,
      #d9e03a 66%,
      var(--lime) 74%,
      #6fc479 83%,
      var(--teal) 91%,
      var(--teal) 100%
    );
  }
  .cover-art {
    position: absolute;
    inset: 0;
    width: 1200px;
    height: 1200px;
  }
  .title-word {
    font-family: "Saira Extra Condensed", "Arial Narrow", sans-serif;
    font-weight: 700;
    font-size: 250px;
    fill: var(--white);
  }
</style>
</head>
<body>
  <main class="cover">
    <svg class="cover-art" viewBox="0 0 1200 1200" xmlns="http://www.w3.org/2000/svg">
      <defs>
        <radialGradient id="emblemGlow" cx="50%" cy="50%" r="50%">
          <stop offset="0%" stop-color="#fef6f0" stop-opacity="0.95"/>
          <stop offset="70%" stop-color="#fef6f0" stop-opacity="0.7"/>
          <stop offset="100%" stop-color="#fef6f0" stop-opacity="0"/>
        </radialGradient>
      </defs>

      <text class="title-word title-top" x="104" y="274" textLength="1000" lengthAdjust="spacingAndGlyphs">LANTERNWAKE</text>

      <ellipse class="emblem-area" role="img" aria-label="Central emblem: a white eye outline with a heart as its pupil"
               cx="600" cy="600" rx="416" ry="219" fill="url(#emblemGlow)"/>

      <text class="title-word title-bottom" x="419" y="1112" textLength="370" lengthAdjust="spacingAndGlyphs">TALES</text>
    </svg>
  </main>
</body>
</html>
```